Dental Medical History Form - Content provided

Design a medical history form for a dental practice. Content is provided so all that is needed is the formatting to make it look great and easy to read.

"Patient Information" to include all information contained in top portion of the "Patient Medical History Form" docx file.

"Medical History" should follow the formatting and content of the "Exact Medical History" file as this is what the entry fields look like in our practice software and so we would like it to match.

1st page - Patient info, allergies, medications, antibiotics, joint replacement, pregnancy.

2nd page - Do you have, or have you had, any of the following? . . . . . . .
Updates

Project Deadline Extended Reason: Picked too short of a deadline to start (2 days) Added Monday, February 13, 2017

Target Market(s)

All ages but must be clear enough for elderly to read. Use as much space as possible to keep font size bigger yet keep to two pages

Industry/Entity Type

Dental

Font styles to use
Sans Serif

Requirements
Must have
• All content provided
• Our logo at the top (file provided)
• Century Gothic Font
• Limit to two pages

```html
<!DOCTYPE html>
<html lang="en">
<head>
<meta charset="utf-8">
<title>Harbour Dental – Patient Medical History</title>
<link href="https://fonts.googleapis.com/css2?family=Mulish:wght@400;600;700&display=swap" rel="stylesheet">
<style>
:root{
  --frame:#7e6a5a;
  --paper:#fdeee6;
  --panel:#ffffff;
  --ink:#3a3535;
  --label:#3d3a3a;
  --soft:#5c5656;
  --rule:#6a6464;
  --box:#c9c4c1;
  --accent:#a89584;
}
*{box-sizing:border-box;margin:0;padding:0}
html,body{width:849px;height:1200px;overflow:hidden;background:var(--frame)}
body{font-family:"Mulish",sans-serif;color:var(--label)}
.sheet{position:absolute;left:14px;top:14px;width:821px;height:1172px;background:var(--paper)}
.page{position:absolute;left:0;top:0;width:849px;height:1200px}
.abs{position:absolute}
.brand{left:48px;top:62px;display:flex;align-items:center;gap:14px;font-size:50px;font-weight:400;color:var(--ink);letter-spacing:-0.5px;line-height:1}
.brand-dot{width:22px;height:22px;border-radius:50%;background:var(--accent)}
.practice{right:52px;top:61px;text-align:right;font-size:13.5px;font-weight:700;line-height:22.5px;color:var(--ink)}
.panel{background:var(--panel);top:179px;height:370px;border:1px solid #f3e6df}
.panel-patient{left:37px;width:382px}
.panel-gp{left:432px;width:382px}
.lbl{font-size:13px;font-weight:700;line-height:16px;white-space:nowrap}
.sub{font-size:13px;font-weight:400;color:var(--soft);line-height:16px}
.tiny{font-size:11px;color:var(--soft);line-height:12px}
.rule{height:1px;background:var(--rule)}
.box{width:22px;height:20px;background:#fff;border:1px solid var(--box)}
.box-dark{border-color:#777}
.opt{font-size:14px;font-weight:400;color:var(--soft);line-height:16px;white-space:nowrap}
.field{left:118px;width:666px;height:26px;background:#fff;border:1px solid var(--box)}
.tick{display:inline-block;vertical-align:-4px;margin:0 4px}
</style>
</head>
<body>
<div class="sheet"></div>
<main class="page">

  <header>
    <div class="abs brand"><span>harbour dental</span><span class="brand-dot"></span></div>
    <address class="abs practice" style="font-style:normal">Harbour Dental<br>3.04/118 Coastline Road<br>Seaview NSW 2261<br>(02) 5550 1234</address>
  </header>

  <section class="abs panel panel-patient"></section>
  <section class="abs panel panel-gp"></section>

  <!-- Patient details -->
  <div class="abs lbl" style="left:51px;top:200px">Name</div><div class="abs lbl" style="left:154px;top:200px">:</div>
  <div class="abs rule" style="left:164px;top:214px;width:249px"></div>
  <div class="abs tiny" style="left:163px;top:222px">Title</div>
  <div class="abs tiny" style="left:203px;top:222px">First</div>
  <div class="abs tiny" style="left:277px;top:222px">Middle</div>
  <div class="abs tiny" style="left:368px;top:222px">Last</div>

  <div class="abs lbl" style="left:51px;top:249px">Address</div><div class="abs lbl" style="left:154px;top:249px">:</div>
  <div class="abs rule" style="left:164px;top:263px;width:249px"></div>
  <div class="abs rule" style="left:164px;top:287px;width:249px"></div>

  <div class="abs lbl" style="left:51px;top:299px">DOB</div><div class="abs lbl" style="left:154px;top:299px">:</div>
  <div class="abs rule" style="left:164px;top:313px;width:249px"></div>
  <div class="abs lbl" style="left:51px;top:324px">Email Address</div><div class="abs lbl" style="left:154px;top:324px">:</div>
  <div class="abs rule" style="left:164px;top:338px;width:249px"></div>

  <div class="abs lbl" style="left:51px;top:349px">Phone Numbers :</div>
  <div class="abs sub" style="left:166px;top:349px">Mobile</div>
  <div class="abs rule" style="left:215px;top:363px;width:198px"></div>
  <div class="abs sub" style="left:166px;top:373px">Work</div>
  <div class="abs rule" style="left:213px;top:387px;width:200px"></div>
  <div class="abs sub" style="left:166px;top:398px">Home</div>
  <div class="abs rule" style="left:213px;top:412px;width:200px"></div>

  <div class="abs lbl" style="left:51px;top:447px">EMERGENCY CONTACT PERSON</div>
  <div class="abs lbl" style="left:51px;top:472px">Name</div><div class="abs lbl" style="left:150px;top:472px">:</div>
  <div class="abs rule" style="left:163px;top:486px;width:250px"></div>
  <div class="abs lbl" style="left:51px;top:497px">Relationship</div><div class="abs lbl" style="left:150px;top:497px">:</div>
  <div class="abs rule" style="left:163px;top:511px;width:250px"></div>
  <div class="abs lbl" style="left:51px;top:522px">Phone number</div><div class="abs lbl" style="left:150px;top:522px">:</div>
  <div class="abs rule" style="left:163px;top:536px;width:250px"></div>

  <!-- GP & health fund -->
  <div class="abs lbl" style="left:448px;top:199px">GENERAL PRACTITIONER</div>
  <div class="abs lbl" style="left:448px;top:232px">Name</div><div class="abs lbl" style="left:548px;top:232px">:</div>
  <div class="abs rule" style="left:561px;top:246px;width:237px"></div>
  <div class="abs lbl" style="left:448px;top:264px">Practice Name :</div>
  <div class="abs rule" style="left:561px;top:278px;width:237px"></div>
  <div class="abs lbl" style="left:448px;top:296px">Phone Number :</div>
  <div class="abs rule" style="left:561px;top:310px;width:237px"></div>
  <div class="abs lbl" style="left:448px;top:330px">Do you have a health fund with dental cover?</div>
  <div class="abs box box-dark" style="left:549px;top:360px"></div>
  <div class="abs lbl" style="left:575px;top:362px">Yes</div>
  <div class="abs sub" style="left:609px;top:362px">or</div>
  <div class="abs box box-dark" style="left:634px;top:360px"></div>
  <div class="abs lbl" style="left:660px;top:362px">No</div>
  <div class="abs lbl" style="left:448px;top:394px">If so, what is the name of the fund ?</div>
  <div class="abs rule" style="left:671px;top:408px;width:127px"></div>
  <div class="abs lbl" style="left:448px;top:427px">Fund Number?&nbsp; :</div>
  <div class="abs rule" style="left:561px;top:441px;width:237px"></div>
  <div class="abs lbl" style="left:448px;top:460px">Priority Number on card &nbsp;: 0 &nbsp;1 &nbsp;2 &nbsp;3 &nbsp;4 &nbsp;&nbsp;5</div>
  <div class="abs box box-dark" style="left:709px;top:458px"></div>
  <div class="abs lbl" style="left:448px;top:492px">Occupation</div><div class="abs lbl" style="left:548px;top:492px">:</div>
  <div class="abs rule" style="left:561px;top:506px;width:237px"></div>
  <div class="abs lbl" style="left:448px;top:525px">Referrred by</div><div class="abs lbl" style="left:548px;top:525px">:</div>
  <div class="abs rule" style="left:561px;top:539px;width:237px"></div>

  <!-- Allergies -->
  <div class="abs lbl" style="left:51px;top:590px">Please indicate if you are allergic to any of the following<svg class="tick" width="19" height="19" viewBox="0 0 19 19"><rect x="1" y="2" width="15" height="15" fill="none" stroke="#3d3a3a" stroke-width="1.6"/><path d="M4 9l4 5 9-13" fill="none" stroke="#3d3a3a" stroke-width="2"/></svg>?</div>
  <div class="abs box" style="left:118px;top:613px"></div><div class="abs opt" style="left:149px;top:615px">Aspirin</div>
  <div class="abs box" style="left:297px;top:613px"></div><div class="abs opt" style="left:328px;top:615px">Codeine</div>
  <div class="abs box" style="left:467px;top:613px"></div><div class="abs opt" style="left:502px;top:615px">Penicillin</div>
  <div class="abs box" style="left:649px;top:613px"></div><div class="abs opt" style="left:682px;top:615px">Sulfites</div>
  <div class="abs box" style="left:118px;top:639px"></div><div class="abs opt" style="left:149px;top:641px">Latex</div>
  <div class="abs box" style="left:297px;top:639px"></div><div class="abs opt" style="left:328px;top:641px">Local Anaesthetic</div>
  <div class="abs box" style="left:467px;top:639px"></div><div class="abs opt" style="left:502px;top:641px">Lactose</div>
  <div class="abs box" style="left:649px;top:639px"></div><div class="abs opt" style="left:682px;top:641px">Nickel</div>
  <div class="abs lbl" style="left:51px;top:677px">Other</div>
  <div class="abs field" style="top:674px"></div>

  <!-- Medication -->
  <div class="abs lbl" style="left:51px;top:718px">Are you currently taking, or have ever taken, any of the following medication<svg class="tick" width="19" height="19" viewBox="0 0 19 19"><rect x="1" y="2" width="15" height="15" fill="none" stroke="#3d3a3a" stroke-width="1.6"/><path d="M4 9l4 5 9-13" fill="none" stroke="#3d3a3a" stroke-width="2"/></svg>?</div>
  <div class="abs box" style="left:118px;top:749px"></div><div class="abs opt" style="left:149px;top:751px">Asthma inhaler</div>
  <div class="abs box" style="left:297px;top:749px"></div><div class="abs opt" style="left:328px;top:751px">Anti-epileptics</div>
  <div class="abs box" style="left:467px;top:749px"></div><div class="abs opt" style="left:502px;top:751px">Anti-depressants</div>
  <div class="abs box" style="left:649px;top:749px"></div><div class="abs opt" style="left:682px;top:751px">Blood Pressure</div>
  <div class="abs box" style="left:118px;top:778px"></div><div class="abs opt" style="left:149px;top:780px">Blood Thinners</div>
  <div class="abs box" style="left:297px;top:778px"></div><div class="abs opt" style="left:328px;top:780px">Bisphosphonates</div>
  <div class="abs box" style="left:467px;top:778px"></div><div class="abs opt" style="left:502px;top:780px">Chemotherapy</div>
  <div class="abs box" style="left:649px;top:778px"></div><div class="abs opt" style="left:682px;top:780px">Insulin</div>
  <div class="abs box" style="left:118px;top:808px"></div><div class="abs opt" style="left:149px;top:810px">Immunosuppressants</div>
  <div class="abs box" style="left:297px;top:808px"></div><div class="abs opt" style="left:328px;top:810px">Steroids</div>
  <div class="abs box" style="left:467px;top:808px"></div><div class="abs opt" style="left:502px;top:810px">Oral Contraceptive</div>
  <div class="abs box" style="left:649px;top:808px"></div><div class="abs opt" style="left:682px;top:810px">Other</div>

  <div class="abs lbl" style="left:51px;top:871px">Please specify medication name, dose, and frequency where possible:</div>
  <div class="abs field" style="top:898px"></div>
  <div class="abs field" style="top:931px"></div>
  <div class="abs field" style="top:964px"></div>

  <!-- Other questions -->
  <div class="abs lbl" style="left:51px;top:1024px">Do you require antibiotic cover ?</div>
  <div class="abs box" style="left:297px;top:1022px"></div><div class="abs opt" style="left:327px;top:1024px">Yes</div>
  <div class="abs box" style="left:370px;top:1022px"></div><div class="abs opt" style="left:399px;top:1024px">No</div>
  <div class="abs lbl" style="left:51px;top:1049px">Have you had a joint replacement?</div>
  <div class="abs box" style="left:297px;top:1047px"></div><div class="abs opt" style="left:327px;top:1049px">Yes</div>
  <div class="abs box" style="left:370px;top:1047px"></div><div class="abs opt" style="left:399px;top:1049px">No</div>
  <div class="abs lbl" style="left:51px;top:1074px">WOMEN</div>
  <div class="abs lbl" style="left:51px;top:1099px">Are you pregnant?</div>
  <div class="abs box" style="left:297px;top:1097px"></div><div class="abs opt" style="left:327px;top:1099px">Yes</div>
  <div class="abs box" style="left:370px;top:1097px"></div><div class="abs opt" style="left:399px;top:1099px">No</div>
  <div class="abs box" style="left:437px;top:1097px"></div><div class="abs opt" style="left:467px;top:1099px">Possible</div>
  <div class="abs lbl" style="left:51px;top:1124px">Breast Feeding?</div>
  <div class="abs box" style="left:297px;top:1122px"></div><div class="abs opt" style="left:327px;top:1124px">Yes</div>
  <div class="abs box" style="left:370px;top:1122px"></div><div class="abs opt" style="left:399px;top:1124px">No</div>

</main>
</body>
</html>
```